Business Card

I need a business card that is fresh, styling and reflects my heart centered healing business while still maintaining full professionalism as I have an my evidence-based practice. I am a Naturopath and a Shiatsu Massage Therapist.
Below are my existing logo (file 1) and an inspiration image (file 2) that reflects the colours and style I would like to express to my card (blues greens). I especially like that tree wallpaper.

Information for the card:
Maren Throsby
BHSc. (Nat) m.ROSC
Naturopath
Herbalist
Nutritionist
Shiatsu Therapist
Wellness Counsellor

47 Dunmore St South Fremantle
www.marenthrosby-demo.com.au
maren@marenthrosby-demo.com.au

NOte: I've removed part of the brief, in that I've changed my mind about the back of the card being a '5 treatments and get sixth one free" I'd rather have this on a separate card. So please do not include this in your designs.

Hi Guys, I've taken the '5 session get the sixth free' part out of the brief. Also, I've added the info to go on the business card into the brief.

Thanks and happy designing
Mar

I've just uploaded a high res better quality version of the hand logo. Thanks Lovlies. 

Target Market(s)

I am targeting western women of ages 25 - 40 in preconception care, sugar addiction therapy, and wellness coaching. I want must card to be vibrant, positive and current.

Industry/Entity Type

Business

Requirements
Must have
• Please include my hand image logo

```html
<!DOCTYPE html>
<html lang="en">
<head>
<meta charset="utf-8">
<title>Maren Throsby – Business Card</title>
<link rel="stylesheet" href="https://fonts.googleapis.com/css2?family=Great+Vibes&family=Arimo:wght@400;700&display=swap">
<style>
  :root {
    --ink-blue: #3a5ad8;
    --royal-blue: #3557de;
    --aqua: #8fd8d4;
    --aqua-light: #b9e8e5;
    --paper: #ffffff;
    --canvas: #ffffff;
  }
  * { box-sizing: border-box; margin: 0; padding: 0; }
  html, body {
    width: 1200px; height: 2220px;
    overflow: hidden;
    background: var(--canvas);
  }
  .sheet { position: relative; width: 1200px; height: 2220px; }

  .card {
    position: absolute;
    width: 584px; height: 1012px;
    overflow: hidden;
  }
  .card--front {
    background: var(--paper);
    font-family: "Arimo", Arial, sans-serif;
    color: var(--ink-blue);
    white-space: nowrap;
  }

  /* Brand mark stand-in */
  .brand {
    position: absolute; left: 30px; top: 90px;
    display: flex; align-items: center; gap: 14px;
    font-weight: 700; font-size: 30px;
    color: var(--ink-blue);
  }
  .brand__dot {
    width: 46px; height: 46px; border-radius: 50%;
    background: var(--ink-blue);
  }

  .practitioner {
    position: absolute; left: 150px; top: 395px;
    font-family: "Great Vibes", cursive;
    font-weight: 400;
    font-size: 66px; line-height: 1;
    color: var(--ink-blue);
  }
  .credentials {
    position: absolute; right: 66px; top: 495px;
    list-style: none; text-align: right;
    font-size: 33px; line-height: 47px;
  }
  .contact {
    position: absolute; left: 72px; top: 822px;
    font-size: 27px; line-height: 52px; font-weight: 700;
  }
  .web-bar {
    position: absolute; left: 0; right: 0; top: 952px;
    height: 52px;
    background: var(--aqua);
    color: var(--paper);
    font-size: 30px; line-height: 52px;
    padding-left: 40px;
  }

  /* Second front: slightly larger type */
  .card--front-large .practitioner { font-size: 72px; top: 392px; }
  .card--front-large .credentials { font-size: 36px; line-height: 49px; top: 498px; }
  .card--front-large .contact { font-size: 29px; line-height: 54px; top: 836px; left: 72px; }
  .card--front-large .web-bar { font-size: 32px; top: 958px; height: 50px; line-height: 50px; }

  /* Backs */
  .pattern-fill { position: absolute; inset: 0; }
  .card--back-aqua .pattern-fill {
    background: linear-gradient(160deg, var(--aqua-light), var(--aqua));
  }
  .card--back-blue .pattern-fill {
    background: linear-gradient(160deg, #4a6ae6, var(--royal-blue));
  }
  .url-band {
    position: absolute;
    top: 110px; bottom: 10px;
    width: 96px;
  }
  .card--back-aqua .url-band { left: 432px; top: 60px; bottom: 60px; }
  .card--back-blue .url-band { left: 254px; background: var(--aqua); }
  .url-vertical {
    position: absolute; left: 50%; top: 50%;
    transform: translate(-50%, -50%) rotate(-90deg);
    white-space: nowrap;
    font-family: "Arimo", Arial, sans-serif;
    font-size: 50px; font-weight: 700;
    color: var(--paper);
  }
</style>
</head>
<body>
<main class="sheet">

  <section class="card card--front" style="left:0; top:0;">
    <div class="brand"><span class="brand__dot"></span>Maren Throsby</div>
    <h1 class="practitioner">Maren Throsby</h1>
    <ul class="credentials">
      <li>BHSc. (Nat) m.ROSC</li>
      <li>Naturopath</li>
      <li>Herbalist</li>
      <li>Nutritionist</li>
      <li>Shiatsu Therapist</li>
      <li>Wellness Counsellor</li>
    </ul>
    <div class="contact">
      <p>47 Dunmore St South Fremantle</p>
      <p>maren@marenthrosby-demo.com.au</p>
    </div>
    <div class="web-bar">www.marenthrosby-demo.com.au</div>
  </section>

  <section class="card card--back-aqua" style="left:612px; top:0;">
    <div class="pattern-fill" role="img" aria-label="White floral lotus and leaf-sprig wallpaper pattern on aqua"></div>
    <div class="url-band"><span class="url-vertical">www.marenthrosby-demo.com.au</span></div>
  </section>

  <section class="card card--front card--front-large" style="left:0; top:1160px;">
    <div class="brand"><span class="brand__dot"></span>Maren Throsby</div>
    <h1 class="practitioner">Maren Throsby</h1>
    <ul class="credentials">
      <li>BHSc. (Nat) m.ROSC</li>
      <li>Naturopath</li>
      <li>Herbalist</li>
      <li>Nutritionist</li>
      <li>Shiatsu Therapist</li>
      <li>Wellness Counsellor</li>
    </ul>
    <div class="contact">
      <p>47 Dunmore St South Fremantle</p>
      <p>maren@marenthrosby-demo.com.au</p>
    </div>
    <div class="web-bar">www.marenthrosby-demo.com.au</div>
  </section>

  <section class="card card--back-blue" style="left:612px; top:1160px;">
    <div class="pattern-fill" role="img" aria-label="White floral lotus and leaf-sprig wallpaper pattern on royal blue"></div>
    <div class="url-band"><span class="url-vertical">www.marenthrosby-demo.com.au</span></div>
  </section>

</main>
</body>
</html>
```